Postcard design for Intellectual Property Professional Conference

Seeking design for 5.5" by 8.5" postcard mailer about a conference on tax and finance issues for international IP management. Attendees are lawyers and financial executives. Draft language is attached.

Target Market(s)

The project should have the attached picture of Boston with the caption "Courtesy of the Harborline Meeting & Travelers Council"

Industry/Entity Type

Finance

```html
<!DOCTYPE html>
<html lang="en">
<head>
<meta charset="utf-8">
<title>IP Tax &amp; Finance Conference Postcard</title>
<link href="https://fonts.googleapis.com/css2?family=Arimo:wght@400;700&family=Tinos&display=swap" rel="stylesheet">
<style>
  :root {
    --navy: #1b2a4e;
    --ink: #1f2d4f;
    --logo-blue: #1f4f8f;
    --white: #ffffff;
    --veil: rgba(255, 255, 255, 0.62);
    --sky-top: #c9dcea;
    --sky-mid: #b7c9d6;
    --tower: #9a8b7c;
    --brick: #a7705a;
    --harbor: #6c7f86;
    --walk: #8a6a5a;
  }
  * { margin: 0; padding: 0; box-sizing: border-box; }
  html, body { width: 1200px; height: 776px; overflow: hidden; background: var(--white); }
  .postcard {
    position: relative;
    width: 1200px;
    height: 776px;
    overflow: hidden;
    font-family: "Arimo", Arial, sans-serif;
    color: var(--ink);
  }
  .harbor-photo {
    position: absolute;
    inset: 0;
    background:
      linear-gradient(180deg, transparent 0%, transparent 58%, rgba(108,127,134,0.55) 70%, rgba(138,106,90,0.8) 86%, var(--walk) 100%),
      linear-gradient(90deg, var(--sky-top) 0%, var(--sky-mid) 30%, var(--tower) 55%, var(--brick) 72%, var(--sky-mid) 88%, var(--sky-top) 100%);
  }
  .photo-credit {
    position: absolute;
    top: 5px;
    right: 8px;
    font-family: "Tinos", "Times New Roman", serif;
    font-size: 17px;
    line-height: 20px;
    color: #111;
    white-space: nowrap;
    text-align: right;
  }
  .topics-panel {
    position: absolute;
    left: 0;
    top: 0;
    width: 588px;
    height: 664px;
    background: var(--veil);
    padding: 12px 0 0 14px;
  }
  .topics-title {
    font-size: 22px;
    font-weight: 700;
    color: var(--navy);
    padding-left: 22px;
    line-height: 26px;
    margin-bottom: 2px;
  }
  .topics-list { list-style: none; width: 520px; }
  .topics-list li {
    position: relative;
    padding-left: 22px;
    font-size: 20.5px;
    line-height: 26.4px;
    color: var(--ink);
  }
  .topics-list li::before {
    content: "";
    position: absolute;
    left: 3px;
    top: 9px;
    width: 9px;
    height: 9px;
    border-radius: 50%;
    background: var(--ink);
  }
  .org-band {
    position: absolute;
    left: 0;
    top: 664px;
    width: 588px;
    height: 112px;
    background: var(--white);
  }
  .org-mark {
    position: absolute;
    left: 190px;
    top: 24px;
    width: 56px;
    height: 56px;
    background: var(--logo-blue);
  }
  .org-name {
    position: absolute;
    left: 266px;
    top: 20px;
    font-size: 23px;
    line-height: 31px;
    font-weight: 700;
    color: var(--logo-blue);
    white-space: nowrap;
  }
  .org-tagline {
    position: absolute;
    left: 133px;
    top: 84px;
    font-size: 13.5px;
    color: var(--navy);
    white-space: nowrap;
  }
  .address-box {
    position: absolute;
    background: var(--white);
    border-radius: 14px;
  }
  .address-box--stamp { left: 1012px; top: 30px; width: 176px; height: 217px; }
  .address-box--mailing { left: 694px; top: 446px; width: 494px; height: 318px; }
</style>
</head>
<body>
<div class="postcard">
  <div class="harbor-photo" role="img" aria-label="Photograph of the Boston HarborWalk with waterfront towers, brick buildings, lamp posts and the harbor under a pale sky"></div>
  <p class="photo-credit">Boston HarborWalk-credit: Harborline Meeting &amp; Travelers Council</p>

  <section class="topics-panel">
    <h2 class="topics-title">TOPICS TO BE COVERED INCLUDE:</h2>
    <ul class="topics-list">
      <li>Market trends in IP tax &amp; legal structures</li>
      <li>Proposed US Tax changes and regulatory developments outside the US including European and OECD developments affecting IP, patent box, base erosion and profit splitting (BEPS)</li>
      <li>Overview of the IP landscape in key developing growth markets such as China, India, Brazil, Korea, South Africa, Mexico and other developing markets outside the US.</li>
      <li>Legal issues including litigation, arbitration and use of government assistance to protect IP values in key developing markets.</li>
      <li>Monetizing IP assets and rights in regard to divestitures, spin offs, split offs, M&amp;A, transfers of ownership and securitizations in developing growth markets</li>
      <li>Special Tax Planning and Legal Considerations for IP in Particular Sectors such as Biopharmaceutical, International Sports Licensing, High Tech, Consumer Brands, and Manufacturing</li>
      <li>Restructuring and Migration of IP Assets to Tax Advantaged Jurisdictions</li>
    </ul>
  </section>

  <footer class="org-band">
    <span class="org-mark"></span>
    <span class="org-name">Meridian Growth<br>Markets Council</span>
    <span class="org-tagline">Focus on tax, law &amp; finance for multinationals</span>
  </footer>

  <div class="address-box address-box--stamp"></div>
  <div class="address-box address-box--mailing"></div>
</div>
</body>
</html>
```